Office services

I need a post card that describes our office services that include Dr. Hollings credentials, services provided and website address, office address and phone number.
I have over 30 years of experience treating patients with chiropractic, acupuncture, and muscle release techniques.
Brandt graduate ( worlds largest chiropractic university)
Fellow, advanced and diplomate of needlework wellness guild of America.(highest certification possible)
Certified in Wexby decompression technique.
Pellman myofascial release certified.

Industry/Entity Type

Office

```html
<!DOCTYPE html>
<html lang="en">
<head>
<meta charset="utf-8">
<title>Lakeview Chiropractor &amp; Acupuncture – Office Postcard</title>
<link rel="stylesheet" href="https://fonts.googleapis.com/css2?family=Cinzel:wght@400;600;700&family=Cabin:wght@400;500;600&family=Dancing+Script:wght@600&display=swap">
<style>
  :root {
    --navy-deep: #0a1b4d;
    --navy: #14327e;
    --royal: #1f4fa3;
    --cyan: #3cc8ea;
    --cyan-light: #62d6f2;
    --ink-blue: #1c3e8c;
    --ink-grey: #4a4f5c;
    --paper: #ffffff;
    --paper-shade: #e6e8ee;
    --stage: #2b2440;
    --photo-skin: #c99a78;
    --photo-dark: #2a2320;
  }
  * { box-sizing: border-box; margin: 0; padding: 0; }
  html, body { width: 1200px; height: 800px; overflow: hidden; }
  body {
    background: var(--stage);
    font-family: "Cabin", sans-serif;
    position: relative;
  }
  .postcard {
    position: absolute;
    top: 213px;
    width: 560px;
    height: 374px;
    overflow: hidden;
    box-shadow: 0 10px 30px rgba(0,0,0,.45);
  }
  .postcard--back { left: 20px; }
  .postcard--front { left: 620px; }

  /* ---------- Back side ---------- */
  .profile-panel {
    position: absolute; left: 0; top: 0; width: 280px; height: 336px;
    background: linear-gradient(180deg, var(--paper) 0%, var(--paper-shade) 100%);
    padding: 0 16px;
  }
  .portrait {
    position: absolute; left: 96px; top: 16px; width: 92px; height: 80px;
    background: linear-gradient(135deg, #8a6a55, var(--photo-skin) 55%, #6d5446);
  }
  .doctor-name {
    position: absolute; left: 0; right: 0; top: 104px; text-align: center;
    font-family: "Cinzel", serif; font-weight: 700; font-size: 17px;
    color: var(--ink-blue); letter-spacing: .5px;
  }
  .credentials {
    position: absolute; left: 16px; right: 12px; top: 132px;
    list-style: none; font-size: 10px; line-height: 12.5px; color: var(--ink-grey);
  }
  .credentials li { padding-left: 12px; position: relative; }
  .credentials li::before {
    content: "✓"; position: absolute; left: 0; color: var(--ink-blue); font-weight: 600;
  }
  .experience {
    position: absolute; left: 16px; top: 304px;
    font-family: "Cinzel", serif; font-weight: 700; font-size: 17px; color: var(--ink-blue);
  }
  .mission-panel {
    position: absolute; left: 280px; top: 0; width: 280px; height: 336px;
    background: radial-gradient(circle at 30% 30%, var(--royal) 0%, var(--navy) 60%, var(--navy-deep) 100%);
    padding: 22px 22px 0 24px; color: var(--paper);
  }
  .mission-heading {
    font-family: "Cinzel", serif; font-weight: 600; font-size: 18px;
    color: var(--cyan); line-height: 20px;
  }
  .mission-text { font-size: 13px; line-height: 16px; margin-bottom: 12px; }
  .contact-band {
    position: absolute; left: 0; bottom: 0; width: 100%; height: 38px;
    display: flex; align-items: center; gap: 10px; padding-left: 18px;
    font-size: 12.5px; letter-spacing: .2px;
  }
  .postcard--back .contact-band {
    background: linear-gradient(90deg, var(--navy-deep), var(--navy));
    color: var(--paper);
  }
  .social-dot { width: 14px; height: 14px; border-radius: 50%; background: var(--paper); flex: none; }

  /* ---------- Front side ---------- */
  .postcard--front {
    background: radial-gradient(circle at 70% 40%, var(--royal) 0%, var(--navy) 50%, var(--navy-deep) 100%);
  }
  .photo-needles {
    position: absolute; left: 150px; top: 0; width: 190px; height: 62px;
    background: linear-gradient(90deg, var(--photo-dark), #6b5a50 50%, var(--photo-dark));
  }
  .photo-massage {
    position: absolute; left: 130px; top: 56px; width: 200px; height: 136px;
    background: linear-gradient(135deg, #e2bc9a, var(--photo-skin) 50%, #a97a5c);
  }
  .brand-name {
    position: absolute; left: 345px; top: 22px;
    font-family: "Cabin", sans-serif; font-weight: 500; font-size: 32px; line-height: 36px;
    letter-spacing: 1px; color: var(--cyan-light);
  }
  .brand-sub {
    position: absolute; left: 347px; top: 62px;
    font-family: "Cinzel", serif; font-size: 10px; color: var(--cyan-light); letter-spacing: .5px;
  }
  .brand-tagline {
    position: absolute; left: 347px; top: 76px; font-size: 8px; color: var(--cyan); letter-spacing: .3px;
  }
  .service-list {
    position: absolute; left: 345px; top: 96px; list-style: none;
    font-size: 12px; line-height: 17px; color: var(--paper);
  }
  .service-list li { padding-left: 15px; position: relative; }
  .service-list li::before {
    content: "✓"; position: absolute; left: 0; color: var(--cyan); font-weight: 600;
  }
  .service-list small { font-size: 9.5px; }
  .call-to-action { position: absolute; left: 24px; top: 204px; color: var(--cyan-light); }
  .call-to-action .headline {
    font-family: "Dancing Script", cursive; font-size: 22px; line-height: 24px;
  }
  .call-to-action .subhead {
    font-family: "Cinzel", serif; font-size: 13.5px; letter-spacing: .3px;
  }
  .call-to-action .phone {
    font-family: "Cabin", sans-serif; font-size: 30px; line-height: 40px; color: var(--cyan);
  }
  .postcard--front .contact-band {
    bottom: 6px;
    background: linear-gradient(180deg, var(--paper) 0%, #c9cdd6 100%);
    color: #1b1f2a;
  }
</style>
</head>
<body>

  <section class="postcard postcard--back" aria-label="Postcard back">
    <div class="profile-panel">
      <div class="portrait" role="img" aria-label="Portrait photo of the doctor"></div>
      <h2 class="doctor-name">Dr. Grant Hollings</h2>
      <ul class="credentials">
        <li>DC – Doctor of Chiropractic, Brandt College of Chiropractic</li>
        <li>Diplomate in Acupuncture</li>
        <li>Diplomate – Meridale Board of Spine Examiners</li>
        <li>Advanced Certification, Needlework Wellness Guild of America</li>
        <li>FNWGA – Fellow of the Needlework Wellness Guild of America</li>
        <li>Certified in Wexby Decompression/Distraction Technique</li>
        <li>Certified in Pellman Myofascial Release Technique</li>
        <li>FKSM – Fellow of the Kestrel Society of Spine Mechanics</li>
      </ul>
      <p class="experience">Over 30 Years Experience</p>
    </div>
    <div class="mission-panel">
      <h3 class="mission-heading">Our Goal</h3>
      <p class="mission-text">To help patients meet their health care goals naturally without drugs or surgery.</p>
      <h3 class="mission-heading">Our Purpose</h3>
      <p class="mission-text">To not only make each patient feel better but actually make them better by correcting the underlying cause.</p>
      <h3 class="mission-heading">Our Philosophy</h3>
      <p class="mission-text">Given the right treatment the human body has an amazing ability to heal itself without drugs.</p>
    </div>
    <div class="contact-band">
      <span class="social-dot"></span>
      <span>Drgranthollings.com • 2840 W Ashbrook Drive, Ste. 114 • Lakeview, IL 61790</span>
    </div>
  </section>

  <section class="postcard postcard--front" aria-label="Postcard front">
    <div class="photo-needles" role="img" aria-label="Photo of acupuncture needles placed in skin"></div>
    <div class="photo-massage" role="img" aria-label="Photo of hands treating a patient's back"></div>

    <p class="brand-name">LAKEVIEW</p>
    <p class="brand-sub">Chiropractor &amp; Acupuncture</p>
    <p class="brand-tagline">Natural Care • Lasting Relief</p>

    <ul class="service-list">
      <li>Migraine headaches</li>
      <li>Neck &amp; back pain, Sciatica</li>
      <li>Shoulder pain <small>including rotator cuff</small></li>
      <li>Knee pain</li>
      <li>Arthritis including rheumatoid</li>
      <li>Muscle pain &amp; stiffness / spasm</li>
      <li>Allergies</li>
      <li>Joint pain</li>
      <li>Trigger points</li>
      <li>Fibromyalgia</li>
      <li>Chronic pain</li>
      <li>Wexby Decompression, <small>certified</small></li>
      <li>Pellman myofascial release, <small>certified</small></li>
    </ul>

    <div class="call-to-action">
      <p class="headline">Chronic Pain? We Can Help!</p>
      <p class="subhead">EASY SAME DAY APPOINTMENTS!</p>
      <p class="phone">555.014.2270</p>
    </div>

    <div class="contact-band">
      <span>Drgranthollings.com • 2840 W Ashbrook Drive, Ste. 114 • Lakeview, IL 61790</span>
    </div>
  </section>

</body>
</html>
```